Stationary for New Company

We need stationary designed for a new company. Details of the required stationary is attached.

The final version should be trendy, clean... only 2 colours (green + grey/black) and professional.

#1: Business Cards (design on 2 sides)
#2: Letterhead (word format)
#3: Cover Page and back cover for proposals
#4: Envelopes,
#5: Thank You card,
#6: Presentation Folder,
#7: Email signatures template (sample attached in word document)

Logo is attached. Logo can be reversed out (will attach once available). Logo can be stacked or horizontal (provided as horizontal).

Files need to be provided in ai + png format.

Target Market(s)

Business owners. More affluent.

Industry/Entity Type

Business

Requirements
Must have
• See brief

Font: Calibri
Should not have
• Photographs / stock photos

```html
<!DOCTYPE html>
<html lang="en">
<head>
<meta charset="utf-8">
<title>Elmwood Insurance Brokers – Stationery Set</title>
<link href="https://fonts.googleapis.com/css2?family=Carlito:wght@400;700&family=Great+Vibes&display=swap" rel="stylesheet">
<style>
  :root{
    --green:#5e8f3a;
    --green-dark:#4f7a30;
    --grey:#6d6e70;
    --grey-light:#e8e8e8;
    --ink:#3a3a3a;
    --paper:#ffffff;
    --stage:#c4c4c4;
  }
  *{box-sizing:border-box;margin:0;padding:0}
  html,body{width:1200px;height:640px;overflow:hidden}
  body{background:var(--stage);font-family:"Carlito",Calibri,sans-serif;color:var(--ink);position:relative}
  .piece{position:absolute;background:var(--paper);overflow:hidden}
  .icon{width:6px;height:6px;fill:var(--grey);flex:none}

  /* brand name block */
  .mark{display:flex;align-items:center;gap:5px;color:var(--green);font-weight:400;line-height:1}
  .mark-square{background:var(--green);flex:none}
  .mark-name{display:flex;flex-direction:column}
  .mark--white{color:#fff}
  .mark--white .mark-square{background:#fff}

  .contact{list-style:none;font-size:6.4px;font-weight:700;color:var(--ink);line-height:1.45}
  .contact li{display:flex;align-items:center;gap:4px}
  .contact .addr{color:var(--green)}

  .decor{position:absolute}

  /* business cards */
  .card{top:14px;width:224px;height:128px;box-shadow:1px 1px 2px rgba(0,0,0,.35)}
  .card--one{left:16px}
  .card--two{left:250px}
  .card--three{left:490px}
  .card--logo{left:726px;display:flex;align-items:center;justify-content:center}
  .card--reverse{left:966px;background:var(--green);display:flex;align-items:center;justify-content:center}
  .card-name{position:absolute;color:var(--green);font-weight:700;font-size:10px}
  .card-name small{font-size:6px;color:var(--grey);font-weight:400}
  .card-title{position:absolute;font-size:6.4px;font-weight:700;color:var(--ink)}
  .card-rule{position:absolute;height:1px;background:#bfbfbf}
  .card--one .card-name{top:12px;right:14px}
  .card--one .card-title{top:25px;right:14px}
  .card--one .card-rule{top:33px;left:0;right:14px}
  .card--one .contact{position:absolute;left:14px;top:52px}
  .card--one .decor{right:6px;bottom:0;width:60px;height:74px;background:var(--green)}
  .card--two .mark{position:absolute;top:14px;right:12px}
  .card--two .card-rule{top:50px;left:12px;right:0;background:var(--green)}
  .card--two .card-name{top:38px;left:12px}
  .card--two .card-title{top:50px;left:12px}
  .card--two .contact{position:absolute;top:72px;left:12px}
  .card--two .contact--right{left:106px;top:70px;border-left:1px solid #bfbfbf;padding-left:6px}
  .card--three .card-name{top:12px;left:130px}
  .card--three .card-title{top:24px;left:130px;font-weight:400}
  .card--three .contact{position:absolute;left:12px;top:52px}
  .card--three .decor{right:6px;bottom:0;width:60px;height:74px;background:#d3dfc8}

  /* letterhead */
  .letterhead{left:16px;top:168px;width:350px;height:454px;box-shadow:1px 1px 3px rgba(0,0,0,.3)}
  .letterhead .mark{position:absolute;top:20px;left:22px}
  .lh-address{position:absolute;top:27px;left:198px;font-size:5.6px;color:var(--green);font-weight:700;line-height:1.4}
  .lh-contact{position:absolute;top:24px;left:260px;border-left:1px solid #bfbfbf;padding-left:4px;font-size:5px}
  .letterhead .decor{right:14px;bottom:34px;width:116px;height:150px;background:var(--grey-light)}
  .band-grey{position:absolute;left:0;bottom:0;width:100%;height:8px;background:var(--grey)}
  .band-green{position:absolute;right:0;bottom:0;height:16px;background:var(--green);clip-path:polygon(6% 0,100% 0,100% 100%,0 100%)}
  .letterhead .band-green{width:142px}

  /* envelopes */
  .env-front{left:215px;top:268px;width:325px;height:150px;box-shadow:2px 2px 4px rgba(0,0,0,.35)}
  .env-front .mark{position:absolute;top:20px;left:16px}
  .env-front .env-address{position:absolute;top:52px;left:30px;font-size:4.6px;line-height:1.4;color:var(--ink)}
  .env-front .decor{right:22px;top:22px;width:80px;height:96px;background:var(--grey-light)}
  .env-front .band-grey{height:7px}
  .env-front .band-green{width:132px;height:14px}
  .env-back{left:392px;top:424px;width:320px;height:160px;box-shadow:2px 2px 4px rgba(0,0,0,.35)}
  .env-back svg{position:absolute;inset:0}
  .env-back .seal{position:absolute;left:138px;top:24px;width:34px;height:34px;background:var(--green)}

  /* presentation folder */
  .folder-closed{left:584px;top:172px;width:288px;height:224px;background:radial-gradient(ellipse at 55% 40%,#6f9e49,var(--green) 70%,var(--green-dark));box-shadow:2px 2px 4px rgba(0,0,0,.35)}
  .folder-closed > .mark{position:absolute;top:16px;right:18px}
  .folder-closed .decor{left:180px;bottom:0;width:72px;height:104px;background:rgba(255,255,255,.3)}
  .folder-pocket{position:absolute;left:0;bottom:0;width:112px;height:62px;background:#fff;border-top-right-radius:100% 100%;border-right:3px solid var(--grey)}
  .folder-pocket .mark{position:absolute;left:8px;top:22px}
  .folder-pocket .contact{position:absolute;left:8px;top:40px;font-size:3px;font-weight:400}
  .folder-open{left:896px;top:172px;width:280px;height:220px;background:linear-gradient(90deg,#6f9e49,var(--green) 48%,var(--green-dark) 50%,#6f9e49);box-shadow:2px 2px 4px rgba(0,0,0,.35)}
  .open-pocket{position:absolute;bottom:0;width:50%;height:72px;background:linear-gradient(#f2f2f2,#fff);display:flex;align-items:center;justify-content:center}
  .open-pocket--left{left:0;clip-path:polygon(0 0,92% 0,100% 100%,0 100%)}
  .open-pocket--right{right:0;clip-path:polygon(8% 0,100% 0,100% 100%,0 100%)}

  /* thank-you card */
  .thanks{left:790px;top:410px;width:142px;height:204px;box-shadow:1px 1px 3px rgba(0,0,0,.3)}
  .thanks-script{position:absolute;top:8px;width:100%;text-align:center;font-family:"Great Vibes",cursive;color:var(--green);font-size:19px}
  .thanks .mark{position:absolute;top:168px;left:42px}
  .thanks-footer{position:absolute;left:0;bottom:0;width:100%;height:16px;background:var(--green);display:flex;align-items:center;justify-content:space-around;padding:0 4px;font-size:3.4px;color:#fff;line-height:1.3}
</style>
</head>
<body>

<svg width="0" height="0" style="position:absolute" aria-hidden="true">
  <symbol id="i-phone" viewBox="0 0 10 10"><path d="M2 0h2l1 3-1.5 1a6 6 0 0 0 2.5 2.5L7 5l3 1v2a2 2 0 0 1-2 2A8 8 0 0 1 0 2a2 2 0 0 1 2-2z"/></symbol>
  <symbol id="i-fax" viewBox="0 0 10 10"><rect x="2" y="0" width="6" height="4"/><rect x="0" y="4" width="10" height="6" rx="1"/></symbol>
  <symbol id="i-web" viewBox="0 0 10 10"><circle cx="5" cy="5" r="4.2" fill="none" stroke-width="1.4"/><path d="M1 5h8M5 1v8" stroke-width="1"/></symbol>
  <symbol id="i-mail" viewBox="0 0 10 10"><rect x="0" y="2" width="10" height="7"/><path d="M0 2l5 4 5-4" fill="none" stroke="#fff" stroke-width="1"/></symbol>
  <symbol id="i-pin" viewBox="0 0 10 10"><path d="M5 0a3.5 3.5 0 0 1 3.5 3.5C8.5 6 5 10 5 10S1.5 6 1.5 3.5A3.5 3.5 0 0 1 5 0z"/></symbol>
</svg>

<!-- Business card: front, version one -->
<section class="piece card card--one">
  <p class="card-name">Martin Cole, <small>BA, CRM</small></p>
  <p class="card-title">President &amp; CEO</p>
  <div class="card-rule"></div>
  <ul class="contact">
    <li><svg class="icon"><use href="#i-phone"/></svg>555.210.4400</li>
    <li><svg class="icon"><use href="#i-phone"/></svg>555.210.7788 (Direct)</li>
    <li><svg class="icon"><use href="#i-fax"/></svg>555.210.4500</li>
    <li><svg class="icon"><use href="#i-phone"/></svg>800.555.0192 (Toll Free)</li>
    <li style="margin-top:4px"><svg class="icon"><use href="#i-web"/></svg>www.elmwoodinsure.example</li>
    <li><svg class="icon"><use href="#i-mail"/></svg>mcole@elmwoodinsure.example</li>
    <li class="addr">2280 Maple Ridge Road, Calgary, AB T2P 1K7</li>
  </ul>
  <div class="decor" role="img" aria-label="Brand accent panel"></div>
</section>

<!-- Business card: front, version two -->
<section class="piece card card--two">
  <div class="mark"><span class="mark-square" style="width:16px;height:16px"></span><span class="mark-name" style="font-size:13px">Elmwood<small style="font-size:6px">Insurance Brokers</small></span></div>
  <p class="card-name">Martin Cole, <small>BA, CRM</small></p>
  <div class="card-rule"></div>
  <p class="card-title" style="top:54px">President &amp; CEO</p>
  <ul class="contact">
    <li><svg class="icon"><use href="#i-phone"/></svg>555.210.4400</li>
    <li><svg class="icon"><use href="#i-phone"/></svg>555.210.7788 (Direct)</li>
    <li><svg class="icon"><use href="#i-fax"/></svg>555.210.4500</li>
    <li><svg class="icon"><use href="#i-phone"/></svg>800.555.0192 (Toll Free)</li>
  </ul>
  <ul class="contact contact--right">
    <li><svg class="icon"><use href="#i-web"/></svg>www.elmwoodinsure.example</li>
    <li><svg class="icon"><use href="#i-mail"/></svg>mcole@elmwoodinsure.example</li>
    <li><svg class="icon"><use href="#i-pin"/></svg>2280 Maple Ridge Road</li>
    <li style="padding-left:10px">Calgary, AB T2P 1K7</li>
  </ul>
</section>

<!-- Business card: front, version three -->
<section class="piece card card--three">
  <p class="card-name">Martin Cole, <small>BA, CRM</small></p>
  <p class="card-title">Designation</p>
  <ul class="contact">
    <li><svg class="icon"><use href="#i-phone"/></svg>555.210.4400</li>
    <li><svg class="icon"><use href="#i-phone"/></svg>555.210.7788 (Direct)</li>
    <li><svg class="icon"><use href="#i-fax"/></svg>555.210.4500</li>
    <li><svg class="icon"><use href="#i-phone"/></svg>800.555.0192 (Toll Free)</li>
    <li style="margin-top:4px"><svg class="icon"><use href="#i-web"/></svg>www.elmwoodinsure.example</li>
    <li><svg class="icon"><use href="#i-mail"/></svg>mcole@elmwoodinsure.example</li>
    <li><svg class="icon"><use href="#i-pin"/></svg>2280 Maple Ridge Road, Calgary, AB T2P 1K7</li>
  </ul>
  <div class="decor" role="img" aria-label="Light brand accent panel"></div>
</section>

<!-- Business card: back, white -->
<section class="piece card card--logo">
  <div class="mark"><span class="mark-square" style="width:40px;height:40px"></span><span class="mark-name" style="font-size:28px">Elmwood<small style="font-size:11px">Insurance Brokers</small></span></div>
</section>

<!-- Business card: back, reversed -->
<section class="piece card card--reverse">
  <div class="mark mark--white"><span class="mark-square" style="width:40px;height:40px"></span><span class="mark-name" style="font-size:28px">Elmwood<small style="font-size:11px">Insurance Brokers</small></span></div>
</section>

<!-- Letterhead -->
<section class="piece letterhead">
  <div class="mark"><span class="mark-square" style="width:30px;height:30px"></span><span class="mark-name" style="font-size:22px">Elmwood<small style="font-size:8px">Insurance Brokers</small></span></div>
  <p class="lh-address">2280 Maple Ridge Road<br>Calgary, AB T2P 1K7</p>
  <ul class="contact lh-contact">
    <li><svg class="icon"><use href="#i-phone"/></svg>555.210.4400</li>
    <li><svg class="icon"><use href="#i-fax"/></svg>555.210.4500</li>
    <li><svg class="icon"><use href="#i-web"/></svg>www.elmwoodinsure.example</li>
    <li><svg class="icon"><use href="#i-mail"/></svg>mcole@elmwoodinsure.example</li>
  </ul>
  <div class="decor" role="img" aria-label="Faint brand accent panel"></div>
  <div class="band-grey"></div>
  <div class="band-green"></div>
</section>

<!-- Envelope front -->
<section class="piece env-front">
  <div class="mark"><span class="mark-square" style="width:22px;height:22px"></span><span class="mark-name" style="font-size:16px">Elmwood<small style="font-size:6px">Insurance Brokers</small></span></div>
  <p class="env-address">mcole@elmwoodinsure.example<br>2280 Maple Ridge Road, Calgary, AB T2P 1K7</p>
  <div class="decor" role="img" aria-label="Faint brand accent panel"></div>
  <div class="band-grey"></div>
  <div class="band-green"></div>
</section>

<!-- Envelope back -->
<section class="piece env-back">
  <svg viewBox="0 0 320 160" width="320" height="160" aria-hidden="true">
    <path d="M0 0 L155 70 L320 0" fill="none" stroke="#c9c9c9" stroke-width="1"/>
    <path d="M0 160 L130 78 M320 160 L180 78" fill="none" stroke="#e0e0e0" stroke-width="1"/>
  </svg>
  <div class="seal" role="img" aria-label="Brand seal square"></div>
</section>

<!-- Presentation folder, closed -->
<section class="piece folder-closed">
  <div class="mark mark--white"><span class="mark-square" style="width:20px;height:20px"></span><span class="mark-name" style="font-size:15px">Elmwood<small style="font-size:6px">Insurance Brokers</small></span></div>
  <div class="decor" role="img" aria-label="Soft brand accent panel"></div>
  <div class="folder-pocket">
    <div class="mark"><span class="mark-square" style="width:12px;height:12px"></span><span class="mark-name" style="font-size:10px">Elmwood<small style="font-size:4px">Insurance Brokers</small></span></div>
    <ul class="contact">
      <li>2280 Maple Ridge Road · 555.210.4400</li>
      <li>Calgary, AB T2P 1K7 · 555.210.4500</li>
    </ul>
  </div>
</section>

<!-- Presentation folder, open -->
<section class="piece folder-open">
  <div class="open-pocket open-pocket--left">
    <div class="mark"><span class="mark-square" style="width:12px;height:12px"></span><span class="mark-name" style="font-size:10px">Elmwood<small style="font-size:4px">Insurance Brokers</small></span></div>
  </div>
  <div class="open-pocket open-pocket--right">
    <div class="mark"><span class="mark-square" style="width:12px;height:12px"></span><span class="mark-name" style="font-size:10px">Elmwood<small style="font-size:4px">Insurance Brokers</small></span></div>
  </div>
</section>

<!-- Thank-you card -->
<section class="piece thanks">
  <p class="thanks-script">Thank You</p>
  <div class="mark"><span class="mark-square" style="width:13px;height:13px"></span><span class="mark-name" style="font-size:10px">Elmwood<small style="font-size:4px">Insurance Brokers</small></span></div>
  <div class="thanks-footer">
    <span>2280 Maple Ridge Road<br>Calgary, AB T2P 1K7</span>
    <span>555.210.4400<br>555.210.4500</span>
    <span>www.elmwoodinsure.example<br>mcole@elmwoodinsure.example</span>
  </div>
</section>

</body>
</html>
```